Western Canadian Survey Company needs Business Card and Letter Head Design

Hello,

We're looking to have our business cards redesigned along with our letterhead.

We've recently changed out logo and would like to use this. Please use some creativity and propose different options (Traditional and modern).

We will provide as much feedback as possible.

Business card should be double sided with our logo. We would also like room for cell phone number, email address and position. Back of the card can just be our logo or potentially a list of our services we provide.

Industry/Entity Type

Business

Contact Information for Business Card

```html
<!DOCTYPE html>
<html lang="en">
<head>
<meta charset="utf-8">
<title>Northline Field Surveys Ltd — Stationery Set</title>
<link rel="stylesheet" href="https://fonts.googleapis.com/css2?family=Michroma&family=Crimson+Text:wght@400;600&display=swap">
<style>
  :root {
    --slate: #4e6b7a;
    --ink: #0d0d0d;
    --paper: #ffffff;
    --stage: #e6e9ed;
    --muted: #5a5f66;
  }
  * { box-sizing: border-box; margin: 0; padding: 0; }
  html, body { width: 1200px; height: 1200px; overflow: hidden; }
  body { background: var(--stage); font-family: "Crimson Text", Georgia, serif; color: var(--muted); position: relative; }

  .wordmark { display: flex; align-items: center; gap: .5em; font-family: "Michroma", sans-serif; font-weight: 400; color: var(--slate); line-height: 1.25; letter-spacing: .04em; }
  .wordmark .mark-square { width: 1.1em; height: 1.1em; background: var(--slate); flex: none; }
  .wordmark.on-dark { color: var(--paper); }
  .wordmark.on-dark .mark-square { background: var(--paper); }

  .brand-hero { position: absolute; left: 0; top: 70px; width: 1200px; display: flex; justify-content: center; }
  .brand-hero .wordmark { font-size: 44px; }

  .sheet { position: absolute; background: var(--paper); box-shadow: 0 3px 14px rgba(40,50,60,.12); overflow: hidden; }

  .letterhead { left: 70px; top: 250px; width: 440px; height: 622px; }
  .letterhead .wordmark { position: absolute; right: 28px; top: 30px; font-size: 12px; }
  .letterhead .footer { position: absolute; left: 30px; bottom: 28px; font-size: 12px; line-height: 1.4; }
  .letterhead .footer .label { color: var(--slate); }

  .envelope { left: 560px; top: 250px; width: 580px; height: 270px; }
  .envelope .wordmark { position: absolute; left: 26px; top: 28px; font-size: 10px; }
  .envelope .return-address { position: absolute; left: 240px; top: 30px; font-size: 12px; line-height: 1.35; }

  .card { width: 300px; height: 172px; }
  .card-front { left: 560px; top: 580px; }
  .card-back { left: 840px; top: 800px; background: var(--ink); }
  .card-front .wordmark { position: absolute; left: 18px; top: 16px; font-size: 8.5px; }
  .card-front .holder { position: absolute; left: 18px; top: 60px; }
  .card-front .name { font-size: 17px; font-weight: 600; color: var(--slate); }
  .card-front .role { font-size: 11px; margin-top: -2px; }
  .card-front .contact { font-size: 9.5px; margin-top: 8px; line-height: 1.35; }
  .card-back .wordmark { position: absolute; left: 22px; top: 50%; transform: translateY(-50%); font-size: 11px; }
</style>
</head>
<body>

  <header class="brand-hero">
    <div class="wordmark"><span class="mark-square"></span><span>NORTHLINE FIELD<br>SURVEYS LTD</span></div>
  </header>

  <section class="sheet letterhead" aria-label="Letterhead">
    <div class="wordmark"><span class="mark-square"></span><span>NORTHLINE FIELD<br>SURVEYS LTD</span></div>
    <div class="footer">
      <p>Dummy City, Dummy Country Land</p>
      <p><span class="label">M.</span>+1 604 555 0148 | <span class="label">E.</span>john@northlinefs.com</p>
    </div>
  </section>

  <section class="sheet envelope" aria-label="Envelope">
    <div class="wordmark"><span class="mark-square"></span><span>NORTHLINE FIELD<br>SURVEYS LTD</span></div>
    <div class="return-address"><p>Dummy City</p><p>Dummy Country Land</p></div>
  </section>

  <section class="sheet card card-front" aria-label="Business card, front">
    <div class="wordmark"><span class="mark-square"></span><span>NORTHLINE FIELD<br>SURVEYS LTD</span></div>
    <div class="holder">
      <p class="name">John Doe</p>
      <p class="role">Director</p>
      <p class="contact">Dummy City, Dummy Country Land<br>M. +1 604 555 0148 | E. john@northlinefs.com</p>
    </div>
  </section>

  <section class="sheet card card-back" aria-label="Business card, back">
    <div class="wordmark on-dark"><span class="mark-square"></span><span>NORTHLINE FIELD<br>SURVEYS LTD</span></div>
  </section>

</body>
</html>
```